Home page design for a business selling commercial cleaning machines

We need a home page web design for a wholesale business selling commercial and industrial cleaning machines and spare parts. There is a huge range of products but we don't want the home page to be too cluttered and confusing.
- The design needs to be practical and functional - sharp corners, lots of white with just accents/splashes of the business colours.
- This is a link to their holding page which is very very basic - http://www.vornaspec.co.nz/ - use this to get the accent colours but please use lots and lots more WHITE in the home page design! There are no colour codes available.
- The attached HPID (home page design information) is in table boxes just to see placement of information. Information in orange text. Words to go on the design in black text.
- Expected standard of design examples:
http://brimalo-aquaforce.com/
http://brimalointernational.com/
http://tovesk.com/
http://www.mulfin.wb.gs/ (different industry)
- Only use Google fonts. Non-responsive. Width 1100pixels. Header height (without nav bar) 150-160 pixels.
- Will need a PSD of the chosen homepage design (CS5 compatible)

```html
<!DOCTYPE html>
<html lang="en">
<head>
<meta charset="utf-8">
<title>Vornaspec – Cleaning Machines</title>
<link rel="stylesheet" href="https://fonts.googleapis.com/css2?family=Open+Sans:wght@400;600;700&family=Arimo:wght@400;700&display=swap">
<style>
:root{
  --orange:#e8531f;
  --orange-dark:#c9410f;
  --orange-light:#f26a2d;
  --ink:#333;
  --grey:#666;
  --panel:#f0f0f0;
  --band:#ededed;
  --line:#ddd;
  --footer:#454545;
  --white:#fff;
}
*{box-sizing:border-box;margin:0;padding:0}
html,body{width:757px;height:1200px;overflow:hidden;background:var(--white)}
body{position:relative;font-family:'Open Sans',sans-serif;color:var(--ink)}
.abs{position:absolute}
.small{font-family:'Arimo',sans-serif}

.logo{left:64px;top:24px;font:700 26px/1 'Open Sans',sans-serif;letter-spacing:1px;color:#555;display:flex;align-items:center;gap:6px}
.logo i{display:inline-block;width:9px;height:9px;background:#888}
.tagline{left:258px;top:13px;width:225px;text-align:center;font-size:10.5px;line-height:13px;color:var(--grey)}
.tagline b{color:var(--orange);font-weight:600}
.service{left:245px;top:65px;font-size:6.5px;color:var(--orange)}
.address{right:58px;top:8px;text-align:right;font-size:7.4px;line-height:14px;font-weight:600;color:#222}
.phone{right:62px;top:42px;font:400 18px/1 'Arimo',sans-serif;color:var(--orange);letter-spacing:.5px}

.nav{left:0;top:84px;width:757px;height:23px;background:linear-gradient(var(--orange-light),var(--orange-dark))}
.nav ul{list-style:none;position:absolute;left:58px;top:0;display:flex;height:23px}
.nav li{font:400 7.4px/23px 'Arimo',sans-serif;color:var(--white);padding:0 8px;border-right:1px solid rgba(255,255,255,.35)}
.nav li.active{background:#5a1e08}
.nav li:nth-child(2){padding:0 7px}

.hero{left:58px;top:122px;width:397px;height:186px;background:linear-gradient(#f4f6f8,#dfe3e6)}
.hero-cap{left:58px;top:286px;width:397px;height:22px;background:rgba(255,255,255,.85);font-size:10.5px;line-height:22px;padding-left:5px;color:#222;font-weight:600}
.hero-cap b{color:var(--orange)}
.why{left:468px;top:122px;width:231px;height:186px;background:var(--panel);padding:5px 7px}
.why h2{font:400 13px/1.2 'Open Sans',sans-serif;color:var(--orange);margin-bottom:4px}
.why ul{list-style:none}
.why li{font:400 6.6px/17.5px 'Arimo',sans-serif;color:#444;padding-left:8px;position:relative}
.why li:before{content:"";position:absolute;left:1px;top:6px;border-left:3px solid #555;border-top:2.5px solid transparent;border-bottom:2.5px solid transparent}

.range{left:0;top:333px;width:757px;height:187px;background:var(--band)}
.range h2{position:absolute;top:16px;width:100%;text-align:center;font:400 13px/1 'Open Sans',sans-serif;letter-spacing:.5px;color:#222}
.card{position:absolute;top:42px;width:97px;height:115px;background:var(--white);border:1px solid #e0e0e0;text-align:center}
.card h3{font:400 8.6px/1 'Open Sans',sans-serif;color:var(--orange);margin-top:6px}
.card .pic{width:64px;height:54px;margin:9px auto 0;background:linear-gradient(#eef0f3,#c9ccd3)}
.btn{display:inline-block;background:var(--orange);color:var(--white);font:700 7.2px/19px 'Open Sans',sans-serif;padding:0 10px;border-radius:4px;border:1px solid #d54410}
.card .btn{position:absolute;left:50%;transform:translateX(-50%);bottom:-9px;white-space:nowrap}

.promo{left:0;top:520px;width:757px;height:56px;background:var(--orange);color:var(--white);text-align:center;font:600 13.2px/18px 'Open Sans',sans-serif;padding-top:10px}
.promo b{font-weight:700}

.feature{top:590px;width:200px;height:150px}
.feature h3{font:700 11px/15px 'Open Sans',sans-serif;letter-spacing:.6px;color:#333}
.feature .pic{margin-top:8px;width:176px;height:76px}
.feature .btn{position:absolute;right:0;bottom:8px}
.vline{top:590px;width:1px;height:155px;border-left:1px dotted #ccc}
.divider{left:58px;top:756px;width:641px;height:2px;background:linear-gradient(90deg,transparent,#e4e4e4,transparent)}

.form-title{left:62px;top:774px;font:600 10.5px/1 'Open Sans',sans-serif;letter-spacing:.3px;color:#333}
.field{height:18px;background:var(--panel);border:1px solid #e2e2e2;font:400 6.8px/16px 'Arimo',sans-serif;color:#555;padding-left:7px}
.list{top:853px;height:109px;background:var(--panel);border:1px solid #e2e2e2;font-family:'Arimo',sans-serif}
.list .hd{height:18px;border-bottom:1px solid #ddd;font-size:6.8px;line-height:18px;padding-left:7px;color:#555}
.list ul{list-style:none;padding:6px 0 0 10px}
.list li{font-size:6.8px;line-height:11.7px;color:#444}
.scroll{position:absolute;right:5px;top:25px;width:6px;height:78px;background:#f8f8f8}
.scroll i{position:absolute;left:0;top:18px;width:6px;height:12px;background:#bbb}
.send{left:550px;top:940px;width:107px;height:24px;background:var(--orange);color:var(--white);font:600 11.5px/22px 'Open Sans',sans-serif;text-align:center;border-radius:5px;border:1px solid #d54410;letter-spacing:.5px}

.brands{left:0;top:980px;width:757px;height:85px;background:var(--band)}
.brands h2{position:absolute;top:13px;width:100%;text-align:center;font:400 14px/1 'Open Sans',sans-serif;letter-spacing:1px;color:#333}
.strip{position:absolute;left:84px;top:42px;width:581px;height:24px;display:flex;background:var(--white)}
.strip span{flex:1;font:700 9px/24px 'Open Sans',sans-serif;color:#333;text-align:center;border-right:1px solid #e2e2e2}
.arrow{position:absolute;top:42px}

.footer{left:0;top:1065px;width:757px;height:135px;background:var(--footer)}
.map{left:72px;top:1080px;width:203px;height:110px;background:linear-gradient(135deg,#b3cdf5,#a9c6f2);border:2px solid var(--white)}
.links{list-style:none;font:400 7px/14px 'Arimo',sans-serif;color:#eee}
.links li:before{content:"";display:inline-block;margin-right:6px;border-left:3px solid var(--orange);border-top:2.5px solid transparent;border-bottom:2.5px solid transparent}
.flogo{left:520px;top:1068px;width:170px;text-align:center;font:700 25px/1 'Open Sans',sans-serif;letter-spacing:1px;color:#ddd;margin-top:23px}
.social{left:547px;top:1133px;display:flex;gap:6px}
.social i{display:block;width:18px;height:18px;border-radius:50%;background:var(--white)}
.copy{left:518px;top:1166px;font:400 6.8px/1 'Arimo',sans-serif;color:#ddd}
</style>
</head>
<body>

<header>
  <div class="abs logo">VORNASPEC <i></i></div>
  <p class="abs tagline"><b>Wholesale importer &amp; distributor of quality Italian industrial,</b> commercial &amp; domestic cleaning machines &amp; accessories</p>
  <p class="abs service small">Service &amp; supply of most makes and models of cleaning machines and spare parts</p>
  <p class="abs address">4 / 27 Tarwin St, Ravensby (office). Open to the public.<br>Head office Harrowdale Coast | Distributors NZ wide</p>
  <p class="abs phone">04 555 0182</p>
</header>

<nav class="abs nav">
  <ul>
    <li class="active">Home</li><li>About</li><li>Water blasters</li><li>Drain cleaners</li><li>Custom machines</li><li>Vacuum Cleaners</li><li>Pumps</li><li>Spare Parts</li><li>PTO machines</li><li>FAQ</li><li>Quote</li><li>Contact</li>
  </ul>
</nav>

<section>
  <div class="abs hero" role="img" aria-label="Bright white showroom with cleaning machines on display"></div>
  <p class="abs hero-cap"><b>Grandura –</b> Hot high pressure washer; strong, reliable, great for daily use</p>
  <aside class="abs why">
    <h2>Why Choose Vornaspec?</h2>
    <ul>
      <li>High quality Italian cleaning machines</li>
      <li>Wide range of brands and models</li>
      <li>Specialist knowledge &amp; expert advice</li>
      <li>Cost of machines – more affordable for top quality</li>
      <li>Able to service and repair all types of cleaning machines</li>
      <li>Huge range of affordable spare parts</li>
      <li>Distributors nationwide offering excellent sales &amp; service support</li>
      <li>Great family business with excellent customer service for</li>
      <li>over 24 years!</li>
    </ul>
  </aside>
</section>

<section class="abs range">
  <h2>HUGE RANGE OF QUALITY CLEANING MACHINES</h2>
  <div class="card" style="left:66px"><h3>Water blasters</h3><div class="pic" role="img" aria-label="Ride-on scrubber machine"></div><span class="btn">More Information</span></div>
  <div class="card" style="left:172px"><h3>Drain cleaners</h3><div class="pic" role="img" aria-label="Three upright drain cleaning units"></div><span class="btn">More Information</span></div>
  <div class="card" style="left:276px"><h3>Custom machines</h3><div class="pic" role="img" aria-label="Ride-on scrubber machine"></div><span class="btn">More Information</span></div>
  <div class="card" style="left:382px"><h3>Vacuum Cleaners</h3><div class="pic" role="img" aria-label="Three upright vacuum units"></div><span class="btn">More Information</span></div>
  <div class="card" style="left:489px"><h3>Pumps high pressure</h3><div class="pic" role="img" aria-label="Ride-on scrubber machine"></div><span class="btn">More Information</span></div>
  <div class="card" style="left:597px"><h3>PTO machines</h3><div class="pic" role="img" aria-label="Three upright machine units"></div><span class="btn">More Information</span></div>
</section>

<section class="abs promo">
  Browse the products, add any item to a quote request form or give us a call for more informa-<br>tion. Not sure what you need? Contact us for expert advice – <b>we’re happy to assist!</b>
</section>

<section>
  <div class="abs feature" style="left:78px">
    <h3>HUGE RANGE OF QUALITY<br>CLEANING MACHINES</h3>
    <div class="pic" role="img" aria-label="Floor polisher and carpet cleaner in a workshop" style="background:linear-gradient(135deg,#4a5a70,#9aa4ae)"></div>
    <span class="btn" style="right:26px;bottom:4px">All Products</span>
  </div>
  <div class="abs vline" style="left:271px"></div>
  <div class="abs feature" style="left:289px">
    <h3>NATIONWIDE DISTRIBUTORS<br>FOR SALES &amp; SERVICING</h3>
    <div class="pic" role="img" aria-label="Map of New Zealand" style="background:linear-gradient(135deg,#aecbf7,#b8d2f5)"></div>
    <span class="btn" style="right:25px;bottom:6px">Contact</span>
  </div>
  <div class="abs vline" style="left:484px"></div>
  <div class="abs feature" style="left:502px">
    <h3>COMPREHENSIVE RANGE<br>OF SPARE PARTS</h3>
    <div class="pic" role="img" aria-label="Spare parts warehouse with staff packing orders" style="background:linear-gradient(135deg,#8a7e68,#c9c2b1)"></div>
    <span class="btn" style="right:24px;bottom:8px">Spare Parts</span>
  </div>
  <div class="abs divider"></div>
</section>

<section>
  <p class="abs form-title">Would you like a Vornaspec representative to contact you? Please fill in the form and we’ll be in touch very soon…</p>
  <div class="abs field" style="left:63px;top:815px;width:140px">First name:</div>
  <div class="abs field" style="left:214px;top:815px;width:140px">Last name:</div>
  <div class="abs field" style="left:365px;top:815px;width:139px">Contact phone:</div>
  <div class="abs field" style="left:516px;top:815px;width:139px">Email Address:</div>

  <div class="abs list" style="left:62px;width:140px">
    <div class="hd">Products / services interested in: *</div>
    <ul><li>Central heating whole house</li><li>Space heating (single rooms)</li><li>Hot water heating</li><li>Gas appliance installation</li><li>Plumbing – new installations</li><li>Plumbing – repairs &amp; maintenance</li><li>Plumbing – (downpipes &amp; spouting)</li></ul>
  </div>
  <div class="abs list" style="left:215px;width:139px">
    <div class="hd">Area you live in : <svg style="position:absolute;right:7px;top:8px" width="5" height="3"><path d="M0 0h5L2.5 3z" fill="#555"/></svg></div>
    <ul><li>Northland</li><li>Auckland</li><li>Coromandel</li><li>Bay of Plenty</li><li>Waikato</li><li>Rotorua</li><li>Eastland</li></ul>
    <div class="scroll"><i></i></div>
  </div>
  <div class="abs field" style="left:384px;top:854px;width:273px;height:76px;line-height:20px">Any further details?:</div>
  <div class="abs send">SEND ENQUIRY</div>
</section>

<section class="abs brands">
  <h2>BRANDS</h2>
  <svg class="arrow" style="left:66px" width="10" height="24"><path d="M8 3L2 12l6 9" stroke="#999" stroke-width="2.5" fill="none"/></svg>
  <div class="strip"><span>Vantelli</span><span>Krestor</span><span>Jetmora</span><span>Aquabrio</span><span>Zelvo</span><span style="flex:1.6;border:0">Pumalink Group</span></div>
  <svg class="arrow" style="left:674px" width="10" height="24"><path d="M2 3l6 9-6 9" stroke="#999" stroke-width="2.5" fill="none"/></svg>
</section>

<footer class="abs footer"></footer>
<div class="abs map" role="img" aria-label="Map of Australia and New Zealand"></div>
<ul class="abs links" style="left:305px;top:1085px"><li>Home</li><li>About</li><li>Meet the Team</li><li>Testimonials</li><li>FAQ</li><li>Quote</li><li>Contact/Map</li></ul>
<ul class="abs links" style="left:405px;top:1086px"><li>Water blasters</li><li>Drain cleaners</li><li>Custom machines</li><li>Vacuum Cleaners</li><li>Pumps high pressure</li><li>Spare Parts</li><li>PTO machines</li></ul>
<div class="abs flogo">VORNASPEC</div>
<div class="abs social"><i></i><i></i><i></i><i></i><i></i></div>
<p class="abs copy">© Copyright Vornaspec LTD. 2010, All Rights Reserved.</p>

</body>
</html>
```